The Timber Loft

We need a business card design for our wardrobe company.
Please visit our website www.zorvelcabinets.com to get an idea of who we are.

```html
<!DOCTYPE html>
<html lang="en">
<head>
<meta charset="utf-8">
<title>The Timber Loft – Business Card</title>
<link href="https://fonts.googleapis.com/css2?family=Roboto:wght@400;500&display=swap" rel="stylesheet">
<style>
  :root {
    --stage: #3a3a3a;
    --card-light: #ffffff;
    --card-dark: #262626;
    --ink: #1c1c1c;
    --ink-soft: #444444;
    --paper-text: #f2f2f2;
    --rule: #3c3c3c;
  }
  * { margin: 0; padding: 0; box-sizing: border-box; }
  html, body {
    width: 1200px; height: 900px; overflow: hidden;
    background: var(--stage);
    font-family: "Roboto", Arial, sans-serif;
  }
  .stage {
    width: 1200px; height: 900px;
    display: flex; flex-direction: column; align-items: center; justify-content: center;
    gap: 40px;
  }
  .card {
    width: 630px; height: 360px; position: relative;
    box-shadow: 0 10px 30px rgba(0,0,0,.35);
  }
  .card--front { background: var(--card-light); color: var(--ink); }
  .card--back { background: var(--card-dark); color: var(--paper-text); }

  .person { position: absolute; left: 40px; top: 44px; }
  .person__name { font-size: 30px; font-weight: 500; letter-spacing: 1px; text-transform: uppercase; }
  .person__role { font-size: 14px; color: var(--ink-soft); margin-top: 2px; }

  .divider { position: absolute; left: 40px; right: 40px; top: 126px; border-top: 1.5px solid var(--rule); }

  .contacts { position: absolute; left: 40px; top: 146px; list-style: none; font-size: 15px; line-height: 23px; }
  .contacts li { display: flex; align-items: center; gap: 10px; }
  .contacts svg { width: 11px; height: 11px; fill: none; stroke: var(--ink-soft); stroke-width: 1.4; }

  .brand { position: absolute; display: flex; align-items: center; gap: 12px; }
  .brand__mark { width: 14px; height: 14px; flex: none; }
  .brand__name { font-weight: 500; text-transform: uppercase; letter-spacing: .5px; }
  .brand__tagline { font-weight: 400; }

  .card--front .brand { right: 40px; top: 44px; }
  .card--front .brand__mark { background: var(--ink); }
  .card--front .brand__name { font-size: 15px; }
  .card--front .brand__tagline { font-size: 13px; color: var(--ink-soft); margin-top: 2px; }

  .address { position: absolute; right: 40px; bottom: 40px; text-align: right; font-size: 16px; line-height: 22px; font-style: normal; }

  .card--back .brand { left: 70px; top: 50%; transform: translateY(-50%); gap: 18px; }
  .card--back .brand__mark { width: 22px; height: 22px; background: var(--paper-text); }
  .card--back .brand__name { font-size: 30px; }
  .card--back .brand__tagline { font-size: 22px; margin-top: 6px; }
</style>
</head>
<body>
<main class="stage">
  <section class="card card--front" aria-label="Card front">
    <div class="person">
      <h1 class="person__name">Dorian Vale</h1>
      <p class="person__role">Director</p>
    </div>

    <div class="brand">
      <span class="brand__mark"></span>
      <div>
        <p class="brand__name">The Timber Loft</p>
        <p class="brand__tagline">Crafted Square and True</p>
      </div>
    </div>

    <div class="divider"></div>

    <ul class="contacts">
      <li><svg viewBox="0 0 12 12"><path d="M3 1 L5 3.5 L4 5 Q5 7 7 8 L8.5 7 L11 9 L9.5 11 Q4 10.5 1 2.5 Z"/></svg>0207 555 0148</li>
      <li><svg viewBox="0 0 12 12"><rect x="1" y="2.5" width="10" height="7"/><path d="M1 2.5 L6 6.5 L11 2.5"/></svg>info@zorvelcabinets.com</li>
      <li><svg viewBox="0 0 12 12"><circle cx="6" cy="6" r="5"/><path d="M1 6 H11 M6 1 Q3 6 6 11 M6 1 Q9 6 6 11"/></svg>www.zorvelcabinets.com</li>
    </ul>

    <address class="address">Marlow Yard, 42 Fenwick Road,<br>London N4 7QT</address>
  </section>

  <section class="card card--back" aria-label="Card back">
    <div class="brand">
      <span class="brand__mark"></span>
      <div>
        <p class="brand__name">The Timber Loft</p>
        <p class="brand__tagline">Crafted Square and True</p>
      </div>
    </div>
  </section>
</main>
</body>
</html>
```